Homebuilder & Remodeling Firm looking for archectrual looking website

We are a Custom home building & remodeling company since 1986 and would like to launch a website.Carl Tondevik the principle of the firm is a graduate of Harwell Univesity school of architecture and draws his own designs and working drawings. and has done many residential, single and multi family projects in the Dallas Ft Worth Metroplex. We want our website to be architectural in design and visually appealing. We will eventually have photos to provide for you. The message we want to communicate is we have current update knowledge with trends, and longevity in experience. Our message is that we are a firm that designs and remodels fully through and we provide a well executed custom home that is unique to each client. The Homes that we build are unique ,authentic and sustainable architectural styles such as mid century modern, contemporary, transitional and they are sophisticated homes to compliment individual lifestyles of our clients. We have a passion for construction and an attention to detail that makes your dreams come to life. We listen to each clients every need in functionality and form and take them from pre-construction to post-construction follow -up.
We help you invest in your home. Thoughts Create Reality

EXAMPLES OF WEBSITES THAT WE LIKE. PLEASE DO
MORE CONTEMPORARY, SLEEK, ARCHITECTURAL

* Please make the LOGO a bigger part of design

http://pellamcrew.build/
https://www.vintrasol.co/
http://dostavanehomes.com/
http://www.milesfardowdesign.com/
http://www.quillmerton.com/
http://fennikdesignstudios.com/about
http://brandelorgc.com/

thank you,

Reason: We have many clients asking to see our website and re ready to launch something for them to look at

Target Market(s)

Home owners, home buyers, interior designers, All ages

Industry/Entity Type

Builders

Coding

Coded - Design and coding required

Number of Pages Required

5+ page

Font styles to use
Sans Serif

Requirements
Must have
• HTML5 OR PHP
• graphic artist must speak English:
• *Visually appealing, user friendly,
• * the website should reflect the stability and integrity of the company since it has been in business for over 30 years
• * a sophistication and refinement is our mandate.
Should not have
• Too busy, too much going on, we want more minimal in design and artsitic

```html
<!DOCTYPE html>
<html lang="en">
<head>
<meta charset="utf-8">
<title>Tondevik Development</title>
<link href="https://fonts.googleapis.com/css2?family=Lato:wght@400;700;900&family=Marcellus&family=Mulish:wght@400;600;700&display=swap" rel="stylesheet">
<style>
:root{
  --navy:#1f2c5c;
  --navy-deep:#17224a;
  --navy-dark:#121a38;
  --ink:#2b2f3a;
  --muted:#7a7f8c;
  --line:#d9dce4;
  --white:#ffffff;
  --paper:#f6f7f9;
}
*{margin:0;padding:0;box-sizing:border-box}
html,body{width:1200px;height:4420px;overflow:hidden}
body{font-family:"Mulish",sans-serif;color:var(--ink);background:var(--white);position:relative}
.heading{font-family:"Marcellus",serif;font-weight:400;color:var(--navy)}
.kicker{font-family:"Mulish",sans-serif;font-size:15px;color:var(--muted);text-align:center;letter-spacing:.5px}
.btn{display:inline-block;font-family:"Lato",sans-serif;font-size:15px;font-weight:700;letter-spacing:.6px;padding:16px 26px;background:var(--navy);color:var(--white);text-decoration:none;text-transform:uppercase}
.btn.ghost{background:transparent;border:2px solid var(--white)}
.photo{position:absolute}

/* header */
.site-header{position:absolute;top:0;left:0;width:1200px;height:120px;background:var(--white);display:flex;align-items:center;justify-content:space-between;padding:0 80px}
.brand{display:flex;align-items:center;gap:14px}
.brand-square{width:44px;height:44px;background:var(--navy)}
.brand-name{font-family:"Marcellus",serif;font-size:26px;color:var(--navy)}
.main-nav{display:flex;gap:8px;align-items:center}
.main-nav a{font-family:"Lato",sans-serif;font-size:15px;font-weight:700;color:var(--navy);text-decoration:none;padding:12px 16px;border-radius:24px}
.main-nav a.active{background:var(--navy);color:var(--white);padding:12px 24px}

/* hero */
.hero{position:absolute;top:120px;left:0;width:1200px;height:552px;background:linear-gradient(160deg,#3a4250 0%,#23262d 45%,#4a3c2c 75%,#1c1e22 100%)}
.hero-shade{position:absolute;inset:0;background:rgba(10,14,30,.35)}
.hero-content{position:absolute;top:140px;left:0;width:100%;text-align:center;color:var(--white)}
.hero-title{font-family:"Lato",sans-serif;font-weight:900;font-size:76px;letter-spacing:2px}
.hero-text{font-size:19px;font-style:italic;margin:18px auto 0;width:720px;line-height:1.5}
.hero-actions{margin-top:58px;display:flex;gap:34px;justify-content:center}
.hero-dots{position:absolute;bottom:32px;left:0;width:100%;display:flex;gap:10px;justify-content:center}
.hero-dots span{width:14px;height:14px;border-radius:50%;border:2px solid var(--white)}
.hero-dots span.on{background:var(--white)}

/* welcome */
.welcome{position:absolute;top:672px;left:0;width:1200px;height:440px;text-align:center;padding-top:64px}
.welcome .heading{font-size:50px;margin-top:6px}
.welcome p{width:1040px;margin:22px auto 0;font-size:15px;line-height:1.75;color:var(--muted)}
.welcome p+p{margin-top:16px}
.welcome .btn{margin-top:30px}

/* feature rows */
.feature{position:absolute;left:0;width:1200px;height:412px}
.feature .panel{position:absolute;top:0;height:412px;background:var(--navy);color:var(--white);padding:54px 44px}
.feature .panel h2{font-family:"Marcellus",serif;font-weight:400;font-size:40px}
.feature .panel p{font-size:15px;line-height:1.75;margin-top:18px;color:#d7dbe8}
.feature .panel .btn.ghost{margin-top:24px;padding:14px 22px}
.building{top:1112px}
.building .photo{left:0;top:0;width:760px;height:412px;background:linear-gradient(120deg,#e9e7e2 0%,#d7cfc2 40%,#b98a5c 62%,#eceae6 100%)}
.building .panel{left:760px;width:440px}
.remodeling{top:1528px}
.remodeling .panel{left:0;width:440px;padding-top:74px}
.remodeling .photo{left:440px;top:0;width:760px;height:412px;background:linear-gradient(100deg,#7b5a3c 0%,#a9825c 30%,#c7d4da 60%,#5f6e7a 100%)}

/* projects */
.projects{position:absolute;top:1940px;left:0;width:1200px;height:1052px;text-align:center;padding-top:76px}
.projects .heading{font-size:56px;margin-top:4px}
.project-grid{position:absolute;top:172px;left:80px;width:1040px;display:grid;grid-template-columns:repeat(3,328px);grid-auto-rows:360px;gap:28px 28px}
.project{position:relative}
.project.p1{background:linear-gradient(180deg,#2b3f73 0%,#6c8bbc 55%,#e8edf2 80%,#5aa0c0 100%)}
.project.p2{background:linear-gradient(160deg,#1b2750 0%,#47577e 60%,#c9c9c9 100%)}
.project.p3{background:linear-gradient(180deg,#7ea0cf 0%,#c4d2e2 40%,#5b4a3a 70%,#3c4a2e 100%)}
.project.p4{background:linear-gradient(160deg,#f2f2f2 0%,#d8dadf 40%,#2a3458 70%,#c9ccd2 100%)}
.project.p5{background:linear-gradient(170deg,#3d5faa 0%,#7a90c0 40%,#8a6846 70%,#6e6a66 100%)}
.project.p6{background:linear-gradient(150deg,#f5f6f7 0%,#e1e4e8 50%,#b8bec6 100%)}
.project-overlay{position:absolute;inset:0;background:rgba(31,44,92,.88);color:var(--white);padding:56px 30px 0}
.project-overlay .tag{font-size:14px;color:#c8cde0}
.project-overlay h3{font-family:"Marcellus",serif;font-weight:400;font-size:28px;margin-top:6px}
.project-overlay p{font-size:14px;line-height:1.7;margin-top:14px;color:#d7dbe8}
.project-overlay svg{margin-top:18px}
.projects .btn{position:absolute;top:968px;left:527px;padding:16px 36px}

/* testimonials */
.testimonials{position:absolute;top:2992px;left:0;width:1200px;height:480px;background:linear-gradient(180deg,#2a3768 0%,#1f2c5c 60%,#27345f 100%);text-align:center;color:var(--white);padding-top:78px}
.testimonials .kicker{color:#c8cde0}
.testimonials h2{font-family:"Marcellus",serif;font-weight:400;font-size:56px;margin-top:2px}
.quote-mark{margin:24px auto 0;width:56px;height:56px;border:2px solid rgba(255,255,255,.6);border-radius:50%;display:flex;align-items:center;justify-content:center}
.testimonials blockquote{width:880px;margin:26px auto 0;font-size:15px;font-style:italic;line-height:1.75;color:#d2d7e6}
.testimonials cite{display:block;margin-top:18px;font-size:14px;font-style:normal;color:#c8cde0}

/* blog */
.blog{position:absolute;top:3472px;left:0;width:1200px;height:576px;text-align:center;padding-top:30px}
.blog .heading{font-size:56px;margin-top:4px}
.blog-grid{position:absolute;top:128px;left:80px;width:1040px;display:grid;grid-template-columns:512px 512px;gap:16px;text-align:left}
.post .photo{position:relative;width:512px;height:230px}
.post.b1 .photo{background:linear-gradient(180deg,#fbfbfb 0%,#e6e6e6 55%,#2d2d2d 70%,#b1302c 82%,#f0f0f0 100%)}
.post.b2 .photo{background:linear-gradient(180deg,#eef1f4 0%,#cfd4da 45%,#3b3f46 65%,#9aa06e 100%)}
.post-head{display:flex;gap:16px;align-items:flex-start;margin-top:-48px;position:relative}
.post-date{width:84px;height:98px;background:var(--navy);color:var(--white);text-align:center;padding-top:14px;flex:none}
.post-date b{display:block;font-family:"Lato",sans-serif;font-size:38px;line-height:1}
.post-date span{font-size:15px}
.post-title{font-family:"Lato",sans-serif;font-weight:900;font-size:16px;color:var(--navy);line-height:1.55;margin-top:60px;text-transform:uppercase}
.post p{font-size:14px;color:var(--muted);line-height:1.7;margin-top:14px}

/* footer */
.site-footer{position:absolute;top:4048px;left:0;width:1200px;height:332px;background:var(--navy);color:var(--white)}
.site-footer h4{font-family:"Lato",sans-serif;font-weight:400;font-size:19px;padding-bottom:10px;border-bottom:1px solid rgba(255,255,255,.35)}
.col{position:absolute;top:40px}
.col-sitemap{left:80px;width:150px}
.col-sitemap ul{list-style:none;margin-top:14px}
.col-sitemap li{font-size:14px;line-height:2;color:#d2d7e6}
.col-contact{left:332px;width:232px}
.contact-form{margin-top:14px;display:flex;flex-direction:column;gap:10px}
.field{background:var(--white);color:#9aa0ad;font-size:13px;height:30px;padding:6px 10px}
.field.msg{height:44px}
.send{align-self:stretch;background:var(--navy-deep);border:1px solid rgba(255,255,255,.5);text-align:center;font-family:"Lato",sans-serif;font-size:14px;font-weight:700;padding:7px 0}
.col-touch{left:600px;width:270px}
.touch-list{list-style:none;margin-top:16px}
.touch-list li{display:flex;gap:12px;align-items:flex-start;font-size:14px;line-height:1.5;color:#d2d7e6;margin-bottom:14px}
.touch-list svg{flex:none;margin-top:2px}
.col-brand{left:920px;width:200px;top:56px;text-align:center}
.col-brand .brand-square{width:70px;height:70px;background:var(--white);margin:0 auto}
.col-brand .brand-name{color:var(--white);font-size:20px;display:block;margin-top:12px}
.socials{display:flex;gap:14px;justify-content:center;margin-top:26px}
.socials span{width:40px;height:40px;border-radius:50%;border:2px solid var(--white)}
.footer-bar{position:absolute;top:4380px;left:0;width:1200px;height:40px;background:var(--navy-dark);color:#c8cde0;font-size:13px;text-align:center;line-height:40px}
</style>
</head>
<body>

<header class="site-header">
  <div class="brand"><span class="brand-square"></span><span class="brand-name">Tondevik Development</span></div>
  <nav class="main-nav">
    <a class="active">HOME</a><a>ABOUT US</a><a>SERVICES</a><a>PROJECTS</a><a>BLOG</a><a>CONTACT US</a>
  </nav>
</header>

<section class="hero" role="img" aria-label="Photo of a modern home with a wooden deck at dusk">
  <div class="hero-shade"></div>
  <div class="hero-content">
    <h1 class="hero-title">RENOVATE YOUR HOME</h1>
    <p class="hero-text">We are a firm that designs and remodels fully through and we provide a well executed custom home that is unique to each client.</p>
    <div class="hero-actions"><a class="btn">Know More</a><a class="btn ghost">Contact Us</a></div>
  </div>
  <div class="hero-dots"><span></span><span></span><span class="on"></span></div>
</section>

<section class="welcome">
  <div class="kicker">Welcome To</div>
  <h2 class="heading">Tondevik Development</h2>
  <p>Lorem Ipsum is simply dummy text of the printing and typesetting industry. Lorem Ipsum has been the industry's standard dummy text ever since the 1500s, when an unknown printer took a galley of type.</p>
  <p>It has survived not only five centuries, but also the leap into electronic typesetting, remaining essentially unchanged. It was popularised in the 1960s with the release of Letraset sheets containing Lorem Ipsum passages, and more recently with the centuries, but also the leap into electronic typesetting, remaining essentially unchanged.</p>
  <a class="btn">Know More</a>
</section>

<section class="feature building">
  <div class="photo" role="img" aria-label="Photo of a bright interior with a floating wooden staircase"></div>
  <div class="panel">
    <h2>Home Building</h2>
    <p>Lorem Ipsum is simply dummy text of the printing and typesetting industry. Lorem Ipsum has been the industry's standard dummy text ever since the 1500s, when an unknown printer took a galley of type and scrambled it to make a type.</p>
    <a class="btn ghost">Know More</a>
  </div>
</section>

<section class="feature remodeling">
  <div class="panel">
    <h2>Remodeling</h2>
    <p>Lorem Ipsum is simply dummy text of the printing and typesetting industry. Lorem Ipsum has been the industry's standard dummy text ever since the 1500s, when an unknown printer took a galley of type and scrambled it to make a type.</p>
    <a class="btn ghost">Know More</a>
  </div>
  <div class="photo" role="img" aria-label="Photo of a glass-walled home under a timber ceiling"></div>
</section>

<section class="projects">
  <div class="kicker">What We Do</div>
  <h2 class="heading">Our Projects</h2>
  <div class="project-grid">
    <div class="project p1" role="img" aria-label="Photo of a white modern house with a pool"></div>
    <div class="project p2" role="img" aria-label="Photo of a modern house at night">
      <div class="project-overlay">
        <div class="tag">Project Title</div>
        <h3>Lorem is simply text</h3>
        <p>Lorem Ipsum is simply dummy text of the printing and typesetting industry. Lorem Ipsum has been the industry's standard dummy text ever since the 1500s, when an unknown printer took a galley.</p>
        <svg width="22" height="14" viewBox="0 0 22 14"><path d="M2 2l9 9 9-9" fill="none" stroke="#fff" stroke-width="3"/></svg>
      </div>
    </div>
    <div class="project p3" role="img" aria-label="Photo of a modern home lit at dusk"></div>
    <div class="project p4" role="img" aria-label="Photo of a white house with a navy entrance"></div>
    <div class="project p5" role="img" aria-label="Photo of a timber-roofed home terrace"></div>
    <div class="project p6" role="img" aria-label="Photo of a bright empty interior"></div>
  </div>
  <a class="btn">View All</a>
</section>

<section class="testimonials" role="img" aria-label="Navy toned backdrop photo of a modern home">
  <div class="kicker">Testimonials</div>
  <h2>What Our Client Say</h2>
  <div class="quote-mark"><svg width="22" height="18" viewBox="0 0 22 18"><path d="M2 18V9C2 4 5 1 9 0v3C6 4 5 6 5 9h4v9zM13 18V9c0-5 3-8 7-9v3c-3 1-4 3-4 6h4v9z" fill="#fff"/></svg></div>
  <blockquote>"Lorem Ipsum is simply dummy text of the printing and typesetting industry. Lorem Ipsum has been the industry's standard dummy text ever since the 1500s, when an unknown printer took a galley of type and scrambled it to make a type specimen book. It has survived."</blockquote>
  <cite>- CLIENT NAME</cite>
</section>

<section class="blog">
  <div class="kicker">New Updates</div>
  <h2 class="heading">Latest Blog</h2>
  <div class="blog-grid">
    <article class="post b1">
      <div class="photo" role="img" aria-label="Photo of a white living room with a red sofa"></div>
      <div class="post-head">
        <div class="post-date"><b>18</b><span>Feb</span></div>
        <h3 class="post-title">Lorem Ipsum is simply dummy text of the printing and typesetting industry.</h3>
      </div>
      <p>Lorem Ipsum is simply dummy text of the printing and typesetting industry. Lorem Ipsum has been the industry's standard dummy text ever since the 1500s, when an unknown printer took a galley &raquo;</p>
    </article>
    <article class="post b2">
      <div class="photo" role="img" aria-label="Photo of a white cubic modern house"></div>
      <div class="post-head">
        <div class="post-date"><b>17</b><span>Feb</span></div>
        <h3 class="post-title">Lorem Ipsum is simply dummy text of the printing and typesetting industry.</h3>
      </div>
      <p>Lorem Ipsum is simply dummy text of the printing and typesetting industry. Lorem Ipsum has been the industry's standard dummy text ever since the 1500s, when an unknown printer took a galley &raquo;</p>
    </article>
  </div>
</section>

<footer class="site-footer">
  <div class="col col-sitemap">
    <h4>Sitemap</h4>
    <ul><li>Home</li><li>About Us</li><li>Services</li><li>Projects</li><li>Blog</li><li>Contact Us</li></ul>
  </div>
  <div class="col col-contact">
    <h4>Contact Us</h4>
    <div class="contact-form">
      <div class="field">Name</div>
      <div class="field">Email</div>
      <div class="field msg">Message</div>
      <div class="send">SEND</div>
    </div>
  </div>
  <div class="col col-touch">
    <h4>Keep in Touch</h4>
    <ul class="touch-list">
      <li><svg width="16" height="16" viewBox="0 0 16 16"><path d="M8 1a5 5 0 0 0-5 5c0 4 5 9 5 9s5-5 5-9a5 5 0 0 0-5-5zm0 7a2 2 0 1 1 0-4 2 2 0 0 1 0 4z" fill="#fff"/></svg><span>Tondevik Development<br>101 Main Street, Suite 2<br>Dallas, TX 75201</span></li>
      <li><svg width="16" height="16" viewBox="0 0 16 16"><path d="M4 1l3 3-2 2c1 2 3 4 5 5l2-2 3 3-2 3C7 15 1 9 1 3z" fill="#fff"/></svg><span>123-456-7890</span></li>
      <li><svg width="16" height="16" viewBox="0 0 16 16"><path d="M1 3h14v10H1z" fill="none" stroke="#fff" stroke-width="1.5"/><path d="M1 3l7 6 7-6" fill="none" stroke="#fff" stroke-width="1.5"/></svg><span>info@tondevikdevelopment.com</span></li>
    </ul>
  </div>
  <div class="col col-brand">
    <div class="brand-square"></div>
    <span class="brand-name">Tondevik Development</span>
    <div class="socials"><span></span><span></span><span></span></div>
  </div>
</footer>
<div class="footer-bar">&copy; Tondevik Development 2017. All Rights Reserved</div>

</body>
</html>
```